Diverse business needs a corporate identity system

Brantow Fielding Holdings Limited is a well established family owned and run business operating in Port Moresby, Papua New Guinea since 1989. As part of taking the business to the next level, we are redoing our branding/corporate identity.

We currently carry out two core business activities servicing corporate clients in the commercial and industrial sectors:
1. Electrical - new installations and maintenance work
2. Construction - mostly commercial & industrial, some residential

We are looking to add the following business activities in near future:
1. IT consulting
2. Property development - business/industrial park, residential complexes, low cost housing
3. Retail of hardware, construction supplies and flat pack furniture & kitchens

We have just completed our logo design here on SketchHarbor and now wanting to design business card and stationery based on our new logo (attached).

Deliverables are:
1. Business card - double sided
2. Letterhead A4

Details to go on the card:
Name: Marcus Trevane
Title: Director
Email: marcus.trevane@brantowfield.com
Tel: +675 3147720, +675 3148815
Office: Section 17 Lot 48, Waravu Light Industrial Area, Port Moresby, Papua New Guinea
Postal: PO Box 419, Waravu, NCD, Papua New Guinea
Website: brantowfield.com

Our services can be listed somewhere on the card:
Electrical, Construction, Property Development, IT Consulting

Details to go on the letterhead:
Brantow Fielding Holdings Ltd.
PO Box 419, Waravu, NCD, Papua New Guinea
Fax: +675 3146603
Email: info@brantowfield.com

For inspiration, I have uploaded some images of business cards we like.

Would be good if the same/similar business card design could be printed both economically (e.g. full coloured both sides, matte card stock) for majority of staff and upscaled to use premium features such as letter pressed, foil etc for use by executives. Otherwise, please provide two separate designs.

Logo text font is nexa bold freefont - please use something from nexa family or another font type that complements it.

Reason: Few designs were submitted. Most were clearly from ready to use templates. No designs really stand out for us at the moment. So we have decided to narrow the focus to just business card and A4 letterhead. And also revised the brief to be completely open to hopefully invite more creative designs.

I have updated the brief to be a lot less restrictive to try and get more creative designs. Also uploaded more images of premium business cards for inspiration.

Industry/Entity Type

Construction

Requirements
Must have
• All designs must conform to printolane specifications. Refer to and download appropriate work file templates from http://www.printolane.com.au/pl/ns/files/UploadResources.aspx?GP=1%2F9%2F2014+12%3A53%3A21+AM&GPS=5829104463&GNF=1&selectedTab=0.
Should not have
• No QR codes and social media links.

```html
<!DOCTYPE html>
<html lang="en">
<head>
<meta charset="utf-8">
<title>BrantowField Business Card</title>
<link rel="stylesheet" href="https://fonts.googleapis.com/css2?family=Exo:wght@400;500;600;700&display=swap">
<style>
  :root {
    --brand-red: #e43b29;
    --brand-yellow: #f9b233;
    --ink: #222222;
    --paper: #ffffff;
    --backdrop: #e9e3d6;
  }
  * { margin: 0; padding: 0; box-sizing: border-box; }
  html, body {
    width: 1200px;
    height: 1000px;
    overflow: hidden;
  }
  body {
    position: relative;
    background: var(--backdrop);
    font-family: "Exo", sans-serif;
  }
  .card {
    position: absolute;
    overflow: hidden;
    box-shadow: 0 2px 6px rgba(0, 0, 0, 0.18);
  }

  /* Front: red services side */
  .card-front {
    left: 162px;
    top: 204px;
    width: 370px;
    height: 596px;
    background: var(--brand-red);
    color: var(--paper);
  }
  .front-brand {
    position: absolute;
    left: 54px;
    top: 289px;
    top: 85px;
    display: flex;
    align-items: center;
    gap: 12px;
  }
  .brand-dot {
    width: 46px;
    height: 46px;
    border-radius: 50%;
    background: var(--paper);
  }
  .front-brand .brand-name {
    font-size: 34px;
    font-weight: 600;
    color: var(--paper);
    letter-spacing: -0.3px;
  }
  .services {
    position: absolute;
    left: 52px;
    top: 214px;
    list-style: none;
  }
  .services-title {
    font-size: 20px;
    font-weight: 500;
    color: var(--brand-yellow);
    margin-bottom: 12px;
  }
  .service-item {
    position: relative;
    padding-left: 12px;
    font-size: 18px;
    line-height: 22px;
    margin-bottom: 16px;
  }
  .service-item::before {
    content: "";
    position: absolute;
    left: 0;
    top: 3px;
    width: 3px;
    height: 16px;
    background: var(--brand-yellow);
  }
  .front-accent {
    position: absolute;
    left: 122px;
    top: 354px;
    width: 244px;
    height: 244px;
    border-radius: 50%;
    background: rgba(255, 255, 255, 0.1);
  }

  /* Back: white contact side */
  .card-back {
    left: 600px;
    top: 201px;
    width: 371px;
    height: 598px;
    background: var(--paper);
    color: var(--ink);
  }
  .back-dot {
    position: absolute;
    left: 262px;
    top: 24px;
    width: 78px;
    height: 78px;
    border-radius: 50%;
    background: var(--brand-red);
  }
  .back-brand {
    position: absolute;
    left: 46px;
    top: 143px;
    font-size: 30px;
    font-weight: 600;
    letter-spacing: -0.3px;
  }
  .row {
    position: absolute;
    left: 46px;
    display: flex;
    align-items: flex-start;
    gap: 10px;
    font-size: 13px;
    line-height: 20px;
  }
  .row svg {
    width: 14px;
    height: 14px;
    margin-top: 3px;
    flex: none;
    fill: none;
    stroke: var(--brand-red);
    stroke-width: 1.4;
    stroke-linecap: round;
    stroke-linejoin: round;
  }
  .address { top: 200px; }
  .holder {
    position: absolute;
    left: 0;
    width: 100%;
    top: 300px;
    text-align: center;
    padding-left: 4px;
  }
  .holder-name {
    font-size: 25px;
    font-weight: 400;
    line-height: 32px;
  }
  .holder-title {
    font-size: 13px;
    margin-top: 2px;
  }
  .contacts {
    position: absolute;
    left: 46px;
    top: 417px;
    list-style: none;
  }
  .contacts .row {
    position: static;
  }
</style>
</head>
<body>

<section class="card card-front">
  <div class="front-brand">
    <span class="brand-dot"></span>
    <span class="brand-name">BrantowField</span>
  </div>
  <ul class="services">
    <li class="services-title">Our services</li>
    <li class="service-item">Electrical</li>
    <li class="service-item">Construction</li>
    <li class="service-item">Property Development</li>
    <li class="service-item">IT Consulting</li>
  </ul>
  <div class="front-accent"></div>
</section>

<section class="card card-back">
  <span class="back-dot"></span>
  <h1 class="back-brand">BrantowField</h1>

  <div class="row address">
    <svg viewBox="0 0 14 14"><path d="M7 13s4.5-4.3 4.5-7.5a4.5 4.5 0 0 0-9 0C2.5 8.7 7 13 7 13z"/><circle cx="7" cy="5.5" r="1.6"/></svg>
    <span>12345 Your Street Adress, Town,<br>State , Country, Zip 90210</span>
  </div>

  <div class="holder">
    <p class="holder-name">Firstname J.Lastname</p>
    <p class="holder-title">Your job Title</p>
  </div>

  <ul class="contacts">
    <li class="row">
      <svg viewBox="0 0 14 14"><circle cx="7" cy="6" r="5"/><path d="M2 6h10M7 1c2 2 2 8 0 10M7 1c-2 2-2 8 0 10M5 13h4"/></svg>
      <span>www.brantowfield.com</span>
    </li>
    <li class="row">
      <svg viewBox="0 0 14 14"><rect x="1" y="3" width="12" height="8"/><path d="M1 3l6 5 6-5"/></svg>
      <span>mail@brantowfield.com</span>
    </li>
    <li class="row">
      <svg viewBox="0 0 14 14"><path d="M3 1.5l2 2.5-1.2 1.5c.8 1.8 2.2 3.2 4 4L9.3 8.3l2.5 2-1.3 2.2C6 12.2 1.8 8 1.5 3.5z"/></svg>
      <span>012 345 6789</span>
    </li>
    <li class="row">
      <svg viewBox="0 0 14 14"><rect x="4" y="1" width="6" height="12" rx="1"/><path d="M6.5 11h1"/></svg>
      <span>012 345 6789</span>
    </li>
    <li class="row">
      <svg viewBox="0 0 14 14"><rect x="1" y="6" width="12" height="6"/><path d="M4 6V2h5l1.5 1.5V6M3.5 9h2"/></svg>
      <span>012 345 6789</span>
    </li>
  </ul>
</section>

</body>
</html>
```